Window company needs new banner

Window company that has 3 focuses needs a new banner ad.

We sell window hardware
We make new sashes and windows
We restore old windows

http://www.tlsashandrenewal.com

I would like to create a new banner ad for our home page. The ad would try to capture the 3 sections listed above. I would also say they are listed in importance. Our main focus is hardware for this ad.

our best pictures are on our website.

Our suppliers websites
http://www.brindle.co.uk
http://www.kelphardware.co.uk
https://www.pellowgoods.com

Target Market(s)

Historical buildings
Restoration contractors
window restorers
DIY home owners
custom window and door fabricators- Trades people

Industry/Entity Type

Home And Garden

Font styles to use
Serif

Requirements
Must have
• Show the high level of quality of our hardware and other services

```html
<!DOCTYPE html>
<html lang="en">
<head>
<meta charset="utf-8">
<title>TL Sash &amp; Renewal — Home</title>
<link href="https://fonts.googleapis.com/css2?family=Jost:wght@400;500&family=Oswald:wght@400&family=Playfair+Display:wght@400;500&family=Architects+Daughter&family=Montserrat:wght@500&display=swap" rel="stylesheet">
<style>
  :root {
    --ink: #1f1a17;
    --paper: #ffffff;
    --accent-red: #ed1c24;
    --stone: #c7cbca;
    --muted-nav: #a8a6a4;
    --hero-grey: #cfcfcf;
    --black: #000000;
    --script-grey: #555555;
  }
  * { margin: 0; padding: 0; box-sizing: border-box; }
  html, body { width: 1200px; height: 687px; overflow: hidden; background: var(--paper); }
  .page { position: relative; width: 1200px; height: 687px; overflow: hidden; }

  .site-nav { position: absolute; left: 0; top: 0; width: 1200px; height: 77px; background: var(--ink); }
  .brand { position: absolute; left: 196px; top: 24px; display: flex; align-items: center; gap: 8px;
    font-family: "Playfair Display", serif; font-weight: 500; font-size: 18px; letter-spacing: 0.5px; color: var(--paper); }
  .brand-mark { width: 22px; height: 22px; background: var(--accent-red); }
  .nav-link { position: absolute; top: 31px; font-family: "Jost", sans-serif; font-weight: 500;
    font-size: 12px; letter-spacing: 1.6px; color: var(--paper); text-transform: uppercase; }
  .nav-link.is-current { color: var(--muted-nav); font-weight: 400; }
  .nav-blog { position: absolute; left: 941px; top: 19px; width: 74px; height: 38px;
    border: 2px solid var(--paper); display: flex; align-items: center; justify-content: center;
    font-family: "Jost", sans-serif; font-weight: 500; font-size: 12px; letter-spacing: 1.6px; color: var(--paper); }

  .tagline { position: absolute; left: 194px; top: 108px; }
  .tagline-main { font-family: "Oswald", sans-serif; font-weight: 400; font-size: 21px; color: var(--black);
    letter-spacing: -0.3px; line-height: 24px; }
  .tagline-script { font-family: "Architects Daughter", cursive; font-size: 24px; color: var(--script-grey); letter-spacing: 3px; line-height: 28px; }
  .divider-bars { position: absolute; left: 364px; top: 102px; }
  .sectors { position: absolute; left: 402px; top: 117px; font-family: "Oswald", sans-serif;
    font-size: 15px; letter-spacing: 2px; line-height: 19px; color: var(--black); }
  .services { position: absolute; right: 186px; top: 104px; text-align: right;
    font-family: "Montserrat", sans-serif; font-weight: 500; font-size: 18px; line-height: 19.5px; color: var(--black); }

  .hero { position: absolute; left: 188px; top: 198px; width: 854px; height: 404px; background: var(--ink); overflow: hidden; }
  .hero-corners { position: absolute; inset: 0; }
  .hero-frame { position: absolute; left: 22px; top: 24px; width: 812px; height: 358px; border: 1px solid var(--paper); }
  .hero-headline { position: absolute; left: 40px; top: 130px; width: 350px; text-align: center;
    font-family: "Playfair Display", serif; font-weight: 400; font-size: 29px; letter-spacing: 8px;
    line-height: 35.5px; color: var(--accent-red); }
  .hero-headline .lead { color: var(--hero-grey); }
  .hero-photo-card { position: absolute; left: 405px; top: 54px; width: 392px; height: 298px;
    background: var(--paper); border-radius: 9px; padding: 10px; }
  .hero-photo { width: 100%; height: 100%;
    background: radial-gradient(ellipse at 50% 50%, #d9b26a 0%, #a9803f 28%, #5e4a33 60%, #2d2620 100%); }

  .feature-tile { position: absolute; top: 621px; width: 272px; height: 66px; }
  .tile-hardware { left: 189px; background: linear-gradient(135deg, #6b4a2e, #b88a60 60%, #d9c3a8); }
  .tile-make { left: 478px; background: linear-gradient(180deg, #8fc0ea 0%, #a9cfee 55%, #7a4a3a 100%); }
  .tile-restore { left: 768px; background: linear-gradient(90deg, #d8d2c6, #f1efe8 50%, #9fbf7a); }
</style>
</head>
<body>
<div class="page">
  <header class="site-nav">
    <div class="brand"><span class="brand-mark"></span>TL Sash &amp; Renewal</div>
    <span class="nav-link is-current" style="left:487px">Home</span>
    <span class="nav-link" style="left:555px">Hardware</span>
    <span class="nav-link" style="left:657px">What We Make</span>
    <span class="nav-link" style="left:789px">What We Restore</span>
    <span class="nav-blog">BLOG</span>
  </header>

  <div class="tagline">
    <div class="tagline-main">Window &amp; Hardware</div>
    <div class="tagline-script">Specialists</div>
  </div>
  <svg class="divider-bars" width="17" height="65" viewBox="0 0 17 65" aria-hidden="true">
    <rect x="0" y="0" width="8" height="65" fill="#000"/>
    <rect x="14" y="0" width="3" height="65" fill="#000"/>
  </svg>
  <div class="sectors">COMMERCIAL<br>RESIDENTIAL</div>
  <div class="services">Hardware<br>New Windows &amp; Doors<br>Complete Restoration Services</div>

  <section class="hero">
    <svg class="hero-corners" width="854" height="404" viewBox="0 0 854 404" aria-hidden="true">
      <polygon points="0,0 78,0 0,78" fill="var(--accent-red)"/>
      <polygon points="854,327 854,404 777,404" fill="var(--stone)"/>
    </svg>
    <div class="hero-frame"></div>
    <h1 class="hero-headline"><span class="lead">WE SELL</span><br>QUALITY<br>WINDOW<br>HARDWARE</h1>
    <div class="hero-photo-card">
      <div class="hero-photo" role="img" aria-label="Close-up of a polished brass sash lock fitted on a timber window"></div>
    </div>
  </section>

  <div class="feature-tile tile-hardware" role="img" aria-label="Woodworking chisel cutting wood shavings"></div>
  <div class="feature-tile tile-make" role="img" aria-label="Brick building roofline under blue sky"></div>
  <div class="feature-tile tile-restore" role="img" aria-label="Restored white sash window interior"></div>
</div>
</body>
</html>
```